Pitch Deck presentation

Design multiple graphics and slides that can be used in a PowerPoint presentation.
4 infographics, text templates and blank templates
Attached you will find the infographics references and a couple of styles we would like to have on the presentations
We prefer a simpler design with not too much background noise or colors(prefer to have whiter backgrounds)
The infographics in the whiteboard should be presented 1 per slide with space on the right side to write text for explanation.
4 total columns will be the equivalent to the 4 different slides with design in the presentation.
Attached you have our colors and logos.
https://vault.pelmorisk.net/share/7qerTn4PwzKcX2mBv8LdYa09HsUfJ3gNe?view=open
You can reach out to me with any questions at my email rbastowick@pelmoriq.com

```html
<!DOCTYPE html>
<html lang="en">
<head>
<meta charset="utf-8">
<title>Haulvane Pitch Deck</title>
<link href="https://fonts.googleapis.com/css2?family=Fira+Sans+Condensed:wght@500;600&family=Fira+Sans:wght@500;600&family=Poppins:wght@400;500;600&display=swap" rel="stylesheet">
<style>
:root{
  --orange:#e8501e;
  --orange-soft:#f26a2e;
  --ink:#2b2b2b;
  --charcoal:#363636;
  --grey:#5c5c5c;
  --paper:#ffffff;
  --mist:#f1f1ef;
  --track:#e3e3e5;
  --blue:#3f54a6;
  --blue-light:#4d86d6;
  --pink:#f690d4;
  --magenta:#d6179a;
  --red:#e2321d;
}
*{margin:0;padding:0;box-sizing:border-box}
html,body{width:1200px;height:1065px;overflow:hidden;background:var(--paper)}
body{position:relative;font-family:"Poppins",sans-serif;color:var(--ink)}
.slide{position:absolute;width:350px;height:197px;background:var(--paper);box-shadow:0 1px 7px rgba(0,0,0,.2);overflow:hidden}
.brand{position:absolute;top:5px;right:4px;font-family:"Fira Sans Condensed",sans-serif;font-weight:600;font-size:11px;letter-spacing:.3px;color:var(--ink)}
.heading{position:absolute;font-family:"Fira Sans",sans-serif;font-weight:600;font-size:9.5px;color:var(--ink);padding-left:6px;white-space:nowrap}
.heading::before{content:"";position:absolute;left:0;top:1px;bottom:1px;width:1.2px;background:var(--orange)}
.heading.center{left:0;right:0;text-align:center;padding-left:0}
.heading.center span{position:relative;padding-left:6px}
.heading.center span::before{content:"";position:absolute;left:0;top:1px;bottom:1px;width:1.2px;background:var(--orange)}
.body-text{position:absolute;font-size:3.9px;line-height:1.65;color:var(--grey)}
.intro{position:absolute;font-size:4.1px;line-height:1.6;color:var(--grey);text-align:center}
.photo{position:absolute}
/* footer */
.foot-site{position:absolute;left:0;bottom:3px;width:76px;height:12px;background:var(--charcoal);display:flex;align-items:center;gap:3px;padding-left:5px;color:#fff;font-size:3.6px}
.foot-site i{width:6px;height:6px;border-radius:50%;background:var(--orange);display:block}
.foot-copy{position:absolute;bottom:7px;font-size:3.5px;color:var(--grey)}
.foot-page{position:absolute;right:4px;bottom:3px;width:23px;height:12px;background:var(--orange);color:#fff;font-size:3.6px;display:flex;align-items:center;justify-content:center}
/* cover */
.cover-panel{position:absolute;left:0;top:0;width:203px;height:197px;background:var(--mist)}
.cover-name{position:absolute;left:11px;top:28px;font-family:"Fira Sans Condensed",sans-serif;font-weight:600;font-size:36px;letter-spacing:.5px;color:var(--ink)}
.cover-tag{position:absolute;left:11px;top:91px;width:165px;font-size:11px;line-height:1.45;color:var(--ink);font-weight:500}
.cover-contacts{position:absolute;left:0;top:144px;list-style:none}
.cover-contacts li{display:flex;align-items:center;height:12.5px;font-size:4.8px;color:var(--ink)}
.cover-contacts li::before{content:"";width:7px;height:1px;background:var(--orange);margin-right:5px}
.cover-contacts b{width:7px;height:7px;border-radius:50%;background:var(--orange);margin-right:6px;display:block}
/* agenda */
.agenda-item{position:absolute;width:126px;height:16px;display:flex;align-items:center;justify-content:space-between;padding:0 10px;font-size:4.2px;color:#fff;box-shadow:0 1px 2px rgba(0,0,0,.25)}
.agenda-item.dark{background:var(--charcoal)}
.agenda-item.warm{background:var(--orange)}
/* services */
.service{position:absolute;width:72px;border-left:.6px solid #c9c9c9;padding-left:5px}
.service-title{display:flex;gap:3px;align-items:flex-end;font-size:4px;font-weight:600;line-height:1.2;color:var(--ink)}
.service-title em{font-style:normal;font-size:11px;line-height:.9;color:var(--orange);font-weight:500}
.service p{font-size:3.3px;line-height:1.65;color:var(--grey);margin-top:4px;text-align:justify}
/* stats */
.donut{position:absolute;top:89px;width:42px;text-align:center}
.donut span{position:absolute;left:0;right:0;top:14px;font-family:"Fira Sans",sans-serif;font-weight:600;font-size:8px;color:var(--magenta)}
.donut small{display:block;margin-top:3px;font-size:4.6px;font-weight:600;color:var(--magenta)}
/* production */
.bar-title{position:absolute;left:79px;top:81px;font-weight:600;font-size:7px;color:var(--blue)}
.bar{position:absolute;left:79px;width:178px;height:8px;background:var(--track)}
.bar-fill{height:100%;background:linear-gradient(90deg,var(--blue),var(--blue-light));position:relative}
.bar-fill span{position:absolute;left:100%;top:-1px;padding-left:5px;font-size:6.5px;font-weight:500;color:var(--blue);white-space:nowrap}
/* break */
.break-bg{position:absolute;inset:0;background:linear-gradient(180deg,#e75c2c 0%,#ee6a35 45%,#e0542a 75%,#ec6434 100%)}
.break-title{position:absolute;left:22px;top:76px;padding-left:9px;font-family:"Fira Sans",sans-serif;font-weight:600;font-size:15.5px;color:#fff;white-space:nowrap}
.break-title::before{content:"";position:absolute;left:0;top:3px;bottom:3px;width:1.2px;background:#fff}
.break-sub{position:absolute;left:22px;top:98px;width:170px;font-size:5.6px;line-height:1.35;color:#fff}
/* history */
.history{position:absolute;left:34px;top:37px;width:284px;list-style:none}
.history li{position:relative;padding-left:6px;font-size:3.9px;line-height:1.6;color:var(--ink);margin-bottom:7.9px}
.history li::before{content:"";position:absolute;left:0;top:1.8px;width:2.6px;height:2.6px;border-radius:50%;background:var(--orange)}
/* closing */
.rule{position:absolute;left:9px;width:332px;height:3.5px;background:var(--orange)}
.close-name{position:absolute;left:209px;top:52px;font-family:"Fira Sans Condensed",sans-serif;font-weight:600;font-size:23px;letter-spacing:.4px;color:var(--ink)}
.close-contact{position:absolute;left:209px;display:flex;gap:6px;align-items:center}
.close-contact svg{width:10px;height:10px;flex:none}
.close-contact small{display:block;font-size:3.4px;color:var(--grey)}
.close-contact b{display:block;font-size:4.5px;font-weight:500;color:var(--ink)}
</style>
</head>
<body>

<!-- Cover -->
<section class="slide" style="left:33px;top:52px">
  <div class="cover-panel"></div>
  <div class="cover-name">HAULVANE</div>
  <p class="cover-tag">Online booking platform for road freight transportation</p>
  <ul class="cover-contacts">
    <li><b></b>www.haulvane.com</li>
    <li><b></b>hello@haulvane.com</li>
    <li><b></b>+1 555 014 2290</li>
  </ul>
  <div class="photo" role="img" aria-label="Red truck with a curtain trailer reflected in a rain puddle under a blue sky" style="left:203px;top:0;width:147px;height:197px;background:linear-gradient(180deg,#4f86c6 0%,#9dbde0 30%,#c54040 45%,#8a8f92 58%,#6f95c2 75%,#a9c3df 100%)"></div>
</section>

<!-- Agenda -->
<section class="slide" style="left:426px;top:52px">
  <div class="brand">HAULVANE</div>
  <h2 class="heading" style="left:154px;top:12px">Agenda</h2>
  <div class="agenda-item dark" style="left:42px;top:34px"><span>01. Agenda</span><span>01</span></div>
  <div class="agenda-item warm" style="left:182px;top:34px"><span>02. About Us</span><span>02</span></div>
  <div class="agenda-item warm" style="left:42px;top:57px"><span>02. Mission &amp; Vision</span><span>03</span></div>
  <div class="agenda-item dark" style="left:182px;top:57px"><span>04. What We Do</span><span>04</span></div>
  <div class="agenda-item dark" style="left:42px;top:80px"><span>03. Our Statistics</span><span>05</span></div>
  <div class="agenda-item warm" style="left:182px;top:80px"><span>06. Our Process</span><span>06</span></div>
  <div class="agenda-item warm" style="left:42px;top:103px"><span>04. Page Break</span><span>07</span></div>
  <div class="agenda-item dark" style="left:182px;top:103px"><span>08. Our History</span><span>08</span></div>
  <div class="agenda-item dark" style="left:42px;top:126px"><span>05. Perspiciatis Unde</span><span>09</span></div>
  <div class="agenda-item warm" style="left:182px;top:126px"><span>10. Our Goals</span><span>10</span></div>
  <div class="agenda-item warm" style="left:42px;top:149px"><span>06. What We Achieve</span><span>11</span></div>
  <div class="agenda-item dark" style="left:182px;top:149px"><span>12. Ending</span><span>12</span></div>
  <div class="foot-site"><i></i>www.haulvane.com</div>
  <div class="foot-copy" style="left:150px">© 2024. All Rights Reserved.</div>
  <div class="foot-page">Page 02</div>
</section>

<!-- About -->
<section class="slide" style="left:818px;top:52px">
  <div class="brand">HAULVANE</div>
  <div class="rule" style="left:41px;top:39px;width:109px;height:1.4px"></div>
  <div class="photo" role="img" aria-label="Row of yellow and white trucks parked at a city depot" style="left:41px;top:44px;width:109px;height:109px;background:linear-gradient(180deg,#8d9299 0%,#b9bcbf 40%,#7f8286 100%)"></div>
  <div class="rule" style="left:41px;top:156px;width:109px;height:1.4px"></div>
  <h2 class="heading" style="left:177px;top:60px">About Us</h2>
  <p class="body-text" style="left:177px;top:78px;width:126px;text-align:justify">Haulvane ranks 23rd among 187 competitors which include Freightora, Lanewise and Cargonest. 10 of its competitors are funded while 2 have exited. Overall, Haulvane and its competitors have raised over $935M in funding across 38 funding rounds involving 105 investors. There are 2 private unicorns and 2 acquired companies in the entire competition set.</p>
  <div class="foot-site"><i></i>www.haulvane.com</div>
  <div class="foot-copy" style="left:150px">© 2024. All Rights Reserved.</div>
  <div class="foot-page">Page 03</div>
</section>

<!-- Vision & Mission -->
<section class="slide" style="left:33px;top:307px">
  <div class="brand">HAULVANE</div>
  <svg class="photo" style="left:0;top:0" width="170" height="197" viewBox="0 0 170 197">
    <polygon role="img" aria-label="Port cranes at sunset" points="41,20 57.5,29.5 57.5,48.5 41,58 24.5,48.5 24.5,29.5" fill="#56606c"/>
    <rect role="img" aria-label="Truck on a highway between fields" x="78" y="38" width="67" height="43" fill="#8a9a78"/>
    <polygon role="img" aria-label="Orange shipping container" points="61,51 76.6,60 76.6,78 61,87 45.4,78 45.4,60" fill="#d9693a"/>
    <polygon role="img" aria-label="Stacked shipping containers" points="77,80 118.6,104 118.6,152 77,176 35.4,152 35.4,104" fill="#c96a3d"/>
    <polygon role="img" aria-label="Container ship at sea" points="142,83 162.8,95 162.8,119 142,131 121.2,119 121.2,95" fill="#4e7ea3"/>
    <polygon role="img" aria-label="Cargo detail" points="127,129 135.7,134 135.7,144 127,149 118.3,144 118.3,134" fill="#7b8793"/>
    <polygon role="img" aria-label="White truck on the road" points="122,154 137.6,163 137.6,181 122,190 106.4,181 106.4,163" fill="#9aa3a8"/>
  </svg>
  <h2 class="heading" style="left:198px;top:44px">Our Vision &amp; Mission</h2>
  <p class="body-text" style="left:198px;top:61px;width:126px">We connect shippers and carriers through one clear booking platform, so every load finds the right truck at a fair price. Our aim is to make road freight simple, visible and dependable for businesses of every size, from a single pallet to a full fleet.</p>
  <p class="body-text" style="left:198px;top:105px;width:126px">Our mission is to cut empty miles, shorten waiting times and give every driver steady work. We build tools that turn planning, tracking and payment into a few taps, helping partners move goods faster and with less waste.</p>
  <div class="foot-site"><i></i>www.haulvane.com</div>
  <div class="foot-copy" style="left:150px">© 2024. All Rights Reserved.</div>
  <div class="foot-page">Page 04</div>
</section>

<!-- What We Do -->
<section class="slide" style="left:426px;top:307px">
  <div class="brand">HAULVANE</div>
  <h2 class="heading center" style="top:18px"><span>What We Do</span></h2>
  <p class="intro" style="left:48px;top:38px;width:262px">We match freight with trusted carriers across the country, handling booking, tracking and billing in one place so your goods arrive on time and your team stays focused on growing the business.</p>
  <div class="service" style="left:28px;top:75px"><div class="service-title"><em>1.</em>FULL TRUCKLOAD (FTL) SHIPPING</div><p>Book a whole trailer for large loads with one driver, one route and live tracking.</p></div>
  <div class="service" style="left:136px;top:75px"><div class="service-title"><em>2.</em>LESS THAN TRUCKLOAD (LTL) SHIPPING</div><p>Share trailer space with other shippers and pay only for the room you use.</p></div>
  <div class="service" style="left:243px;top:75px"><div class="service-title"><em>3.</em>EXPRESS AND SAME-DAY DELIVERY</div><p>Urgent goods picked up within hours and delivered the same day across town.</p></div>
  <div class="service" style="left:28px;top:125px"><div class="service-title"><em>4.</em>CROSS-BORDER TRANSPORTATION</div><p>Customs papers and border crossings handled by carriers who know each route.</p></div>
  <div class="service" style="left:136px;top:125px"><div class="service-title"><em>5.</em>TEMPERATURE-CONTROLLED FREIGHT</div><p>Chilled and frozen trailers that keep food and medicine at a steady temperature.</p></div>
  <div class="service" style="left:243px;top:125px"><div class="service-title"><em>6.</em>HAZARDOUS MATERIAL TRANSPORT</div><p>Certified drivers and approved trailers for moving regulated goods with care.</p></div>
  <div class="foot-site"><i></i>www.haulvane.com</div>
  <div class="foot-copy" style="left:150px">© 2024. All Rights Reserved.</div>
  <div class="foot-page">Page 05</div>
</section>

<!-- Statistics -->
<section class="slide" style="left:818px;top:307px">
  <div class="brand">HAULVANE</div>
  <h2 class="heading center" style="top:29px"><span>Our Statistics</span></h2>
  <p class="intro" style="left:40px;top:49px;width:270px">A look at how our on-time delivery and customer satisfaction rates have grown year by year across the whole carrier network.</p>
  <div class="donut" style="left:50px"><svg width="42" height="42" viewBox="0 0 42 42"><circle cx="21" cy="21" r="17.5" fill="none" stroke="var(--pink)" stroke-width="6"/><circle cx="21" cy="21" r="17.5" fill="none" stroke="var(--red)" stroke-width="6" stroke-dasharray="82.5 110" transform="rotate(-90 21 21)"/></svg><span>75%</span><small>2015</small></div>
  <div class="donut" style="left:103px"><svg width="42" height="42" viewBox="0 0 42 42"><circle cx="21" cy="21" r="17.5" fill="none" stroke="var(--pink)" stroke-width="6"/><circle cx="21" cy="21" r="17.5" fill="none" stroke="var(--red)" stroke-width="6" stroke-dasharray="99 110" transform="rotate(-90 21 21)"/></svg><span>90%</span><small>2016</small></div>
  <div class="donut" style="left:156px"><svg width="42" height="42" viewBox="0 0 42 42"><circle cx="21" cy="21" r="17.5" fill="none" stroke="var(--pink)" stroke-width="6"/><circle cx="21" cy="21" r="17.5" fill="none" stroke="var(--red)" stroke-width="6" stroke-dasharray="66 110" transform="rotate(-90 21 21)"/></svg><span>60%</span><small>2017</small></div>
  <div class="donut" style="left:209px"><svg width="42" height="42" viewBox="0 0 42 42"><circle cx="21" cy="21" r="17.5" fill="none" stroke="var(--pink)" stroke-width="6"/><circle cx="21" cy="21" r="17.5" fill="none" stroke="var(--red)" stroke-width="6" stroke-dasharray="104.5 110" transform="rotate(-90 21 21)"/></svg><span>95%</span><small>2018</small></div>
  <div class="donut" style="left:263px"><svg width="42" height="42" viewBox="0 0 42 42"><circle cx="21" cy="21" r="17.5" fill="none" stroke="var(--pink)" stroke-width="6"/><circle cx="21" cy="21" r="17.5" fill="none" stroke="var(--red)" stroke-width="6" stroke-dasharray="27.5 110" transform="rotate(-90 21 21)"/></svg><span>25%</span><small>2019</small></div>
  <div class="foot-site"><i></i>www.haulvane.com</div>
  <div class="foot-copy" style="left:150px">© 2024. All Rights Reserved.</div>
  <div class="foot-page">Page 06</div>
</section>

<!-- Production -->
<section class="slide" style="left:33px;top:562px">
  <div class="brand">HAULVANE</div>
  <h2 class="heading" style="left:141px;top:29px">Our Production</h2>
  <p class="intro" style="left:44px;top:49px;width:262px">Freight volume moved through the platform each year, measured in tonnes across all of our routes and service types.</p>
  <div class="bar-title">Production</div>
  <div class="bar" style="top:100px"><div class="bar-fill" style="width:47px"><span>241 T</span></div></div>
  <div class="bar" style="top:117px"><div class="bar-fill" style="width:75px"><span>432 T</span></div></div>
  <div class="bar" style="top:134px"><div class="bar-fill" style="width:112px"><span>600 T</span></div></div>
  <div class="bar" style="top:151px"><div class="bar-fill" style="width:139px"><span>721 T</span></div></div>
  <div class="foot-site"><i></i>www.haulvane.com</div>
  <div class="foot-copy" style="left:150px">© 2024. All Rights Reserved.</div>
  <div class="foot-page">Page 07</div>
</section>

<!-- Page Break -->
<section class="slide" style="left:426px;top:562px">
  <div class="break-bg" role="img" aria-label="City skyline and container ships on a river, toned orange"></div>
  <h2 class="break-title">Delivering goods, driving progress.</h2>
  <p class="break-sub">Reliable freight booking that keeps your goods and your business moving forward.</p>
</section>

<!-- History -->
<section class="slide" style="left:818px;top:562px">
  <div class="brand">HAULVANE</div>
  <h2 class="heading center" style="top:12px"><span>Our History</span></h2>
  <ul class="history">
    <li>The company began as a small dispatch desk serving local farms and warehouses, matching a handful of trucks with weekly loads by phone and keeping every booking on paper before the first online tools arrived.</li>
    <li>Our first web booking platform launched with forty partner carriers, letting shippers compare prices and reserve trailer space in minutes, which quickly doubled the number of loads moved each month across the region.</li>
    <li>A new mobile app gave drivers live job offers, digital paperwork and same-week payment, helping independent carriers fill empty return trips and cutting average waiting times at loading docks by almost half.</li>
    <li>Expansion into cross-border and temperature-controlled freight opened routes to new markets, supported by a growing team of planners who work around the clock to keep every shipment safe and on schedule.</li>
    <li>Today the network links thousands of verified carriers with businesses of every size, and we continue to invest in smarter routing, cleaner fleets and clear pricing for everyone who moves goods by road.</li>
  </ul>
  <div class="foot-site"><i></i>www.haulvane.com</div>
  <div class="foot-copy" style="left:150px">© 2024. All Rights Reserved.</div>
  <div class="foot-page">Page 09</div>
</section>

<!-- Closing -->
<section class="slide" style="left:426px;top:818px">
  <div class="rule" style="top:4px"></div>
  <div class="photo" role="img" aria-label="Cargo ship leaving a port with cranes at sunset" style="left:31px;top:46px;width:158px;height:106px;border:2px solid var(--orange);border-radius:2px;background:linear-gradient(180deg,#f3b98f 0%,#f6d2b4 40%,#9a6a58 62%,#3f5770 100%)"></div>
  <div class="close-name">HAULVANE</div>
  <div class="close-contact" style="top:94px">
    <svg viewBox="0 0 10 10"><circle cx="5" cy="5" r="4.5" fill="none" stroke="var(--orange)" stroke-width=".6"/><path d="M3.3 3c.2-.3.6-.3.8 0l.4.6-.4.5c.3.6.7 1 1.3 1.3l.5-.4.6.4c.3.2.3.6 0 .8-.9.6-3.6-1.8-3.2-3.2z" fill="var(--orange)"/></svg>
    <div><small>Call Us</small><b>+1 555 014 2290</b></div>
  </div>
  <div class="close-contact" style="top:113px">
    <svg viewBox="0 0 10 10"><circle cx="5" cy="5" r="4.5" fill="none" stroke="var(--orange)" stroke-width=".6"/><rect x="2.8" y="3.4" width="4.4" height="3.2" fill="var(--orange)"/><path d="M2.8 3.4 5 5.1 7.2 3.4" fill="none" stroke="#fff" stroke-width=".4"/></svg>
    <div><small>Email</small><b>hello@haulvane.com</b></div>
  </div>
  <div class="close-contact" style="top:131px">
    <svg viewBox="0 0 10 10"><circle cx="5" cy="5" r="4.5" fill="none" stroke="var(--orange)" stroke-width=".6"/><path d="M5 7.6C3.8 6.2 3.3 5.3 3.3 4.5a1.7 1.7 0 0 1 3.4 0c0 .8-.5 1.7-1.7 3.1z" fill="var(--orange)"/><circle cx="5" cy="4.5" r=".6" fill="#fff"/></svg>
    <div><small>Address</small><b>1482 Corvel Avenue, Marlow Bay, CA 90210</b></div>
  </div>
  <div class="rule" style="top:189px"></div>
</section>

</body>
</html>
```